Help Lu Wenshao redesign his business card!

Lu Wenshao, an "influential" Chinese businessman, made international headlines this week with his business card...but not for the right reasons. Help Lu Wenshao redesign his new business card - funny and/or satirical submissions welcome!

Check out his hilarious business card that he was giving out on a trip to New York, with not one, not two...but TEN titles! Let's just say they're not the most humble titles either :).

Read more about Lu's business card here: http://notes.dailyledgerpost.example/asiadesk/2014/01/14/lu-wenshaos-business-card-needs-to-be-recycled/

While the rest of the world is laughing at him, we want to help. This is an unofficial contest, but we'd like the PixelGuild community to have a shot at redesigning Lu's business card. Thousands of businesses have used PixelGuild.example to create beautiful business cards, so we know the community of designers here can do a great job.

We'd like you to create a business card worthy of this honorable businessman, while also keeping a clean, dignified design.

Funny / satirical job titles and designs are encouraged. Note you do not have to use all of Lu's titles on the card. Feel free to come up with your own creative titles!

In regard to contact details, please use dummy contact details. Lu's company name and street address are:

China Meiling-Ta Reusable Scrap & Recovery Corporation
Baitang Road 7, Qiaoxin District, Nanjing, China

You can design a single sided or double-sided card - it's completely up to you!

We've put $200 up for grabs for the winning entry, which we will email to Lu in an effort to have him using a much more stylish card. Who knows, you might just have China's most important businessman using your design.

Target Market(s)

Business people and government officials of the world

Industry/Entity Type

Business

Font styles to use
Serif
Sans Serif
Decorative

Colors
ec2027
ffc214
6b449b
0455a3

Requirements
Must have
• At least 1 title, preferably more than 1.

Designers can approach this task how they like however one option could be to use one of Lu's titles and create a suitable business card graphic to suit the role. Designers are also encouraged to o make up a new title and design a graphic to suit.

Here are the titles - but you can also make up your own!

Most Generous Host of the Province
Most Noted Benefactor of the Region
Civic Virtue Ambassador
Flood Relief Volunteer Leader
Most well-known and Beloved Chinese Role Model
Top Ten Most Tireless Neighbour
Most Cheerful Donor of the Year
Green Transit Pioneer
Environmental Protection Top Advocate
Nanjing's Finest Urban Renewal Salvage Specialist
Should not have
• No black borders around photographs of Lu Wenshao
Do not present Lu Wenshao's image in grayscale (black and white)

For a detailed guideline for colors to avoid in design targeting the Chinese market, see http://www.quarrystoneadvisors.example/2011/01/17/color/

```html
<!DOCTYPE html>
<html lang="en">
<head>
<meta charset="utf-8">
<title>Wenshao Lu – Business Card</title>
<link rel="stylesheet" href="https://fonts.googleapis.com/css2?family=Open+Sans:wght@400;700&display=swap">
<style>
  :root {
    --backdrop: #8c8c8c;
    --card-white: #ffffff;
    --forest: #0b6b35;
    --lime: #8dc63f;
    --ink: #1a1a1a;
    --portrait-sky: #a9c4dc;
    --portrait-suit: #23252c;
  }
  * { box-sizing: border-box; margin: 0; padding: 0; }
  html, body { width: 1200px; height: 900px; overflow: hidden; }
  body {
    background: var(--backdrop);
    font-family: "Open Sans", Arial, sans-serif;
    position: relative;
  }
  .card {
    position: absolute;
    left: 120px; top: 175px;
    width: 960px; height: 550px;
    background: var(--card-white);
    overflow: hidden;
  }
  .edge-band { position: absolute; left: 0; width: 28px; }
  .edge-band--forest { top: 40px; height: 250px; background: var(--forest); }
  .edge-band--lime { top: 290px; bottom: 0; background: var(--lime); }
  .side-bar { position: absolute; right: 0; top: 232px; bottom: 0; width: 26px; background: var(--lime); }
  .portrait {
    position: absolute; left: 44px; top: 36px; width: 220px; height: 292px;
    background: linear-gradient(180deg, var(--portrait-sky) 0%, #c3d3e2 45%, var(--portrait-suit) 78%, var(--portrait-suit) 100%);
  }
  .identity { position: absolute; left: 292px; top: 24px; right: 26px; color: var(--ink); }
  .name { font-size: 34px; font-weight: 700; color: var(--forest); letter-spacing: .5px; line-height: 1.2; }
  .rule { height: 2px; background: var(--forest); margin: 6px 0 6px; }
  .role { font-size: 22px; line-height: 1.5; }
  .contact { font-size: 22px; line-height: 1.55; display: flex; align-items: center; gap: 8px; }
  .contact svg { width: 20px; height: 20px; flex: none; }
  .company { font-size: 20px; font-weight: 700; color: var(--forest); margin-top: 8px; line-height: 1.4; }
  .address { font-size: 21px; line-height: 1.5; }
  .postal-label { font-weight: 700; color: var(--forest); margin-left: 10px; }
  .honours {
    position: absolute; left: 44px; top: 338px; right: 40px;
    list-style: none; color: var(--lime); font-size: 23px; line-height: 40px;
    white-space: nowrap;
  }
  .sep { margin: 0 10px; }
</style>
</head>
<body>
  <article class="card">
    <div class="edge-band edge-band--forest"></div>
    <div class="edge-band edge-band--lime"></div>
    <div class="side-bar"></div>

    <div class="portrait" role="img" aria-label="Portrait photograph of Wenshao Lu in a dark suit and tie"></div>

    <section class="identity">
      <h1 class="name">WENSHAO LU</h1>
      <div class="rule"></div>
      <p class="role">CEO</p>
      <p class="contact">
        <svg viewBox="0 0 20 20"><rect width="20" height="20" rx="2" fill="#0b6b35"/><rect x="6.5" y="3.5" width="7" height="13" rx="1.2" fill="none" stroke="#fff" stroke-width="1.6"/></svg>
        0123 456 789
      </p>
      <p class="contact">
        <svg viewBox="0 0 20 20"><rect width="20" height="20" rx="2" fill="#0b6b35"/><rect x="3.5" y="5.5" width="13" height="9" fill="none" stroke="#fff" stroke-width="1.5"/><path d="M3.5 5.5 L10 11 L16.5 5.5" fill="none" stroke="#fff" stroke-width="1.5"/></svg>
        wenshaolu@meiling-ta.example
      </p>
      <p class="company">CHINA MEILING-TA</p>
      <p class="address">Reusable Scrap &amp; Recovery Corporation</p>
      <p class="address">1100 Uknow Street, Anywhere, Any City <span class="postal-label">Postal Code:</span> 284317</p>
      <p class="contact">
        <svg viewBox="0 0 20 20"><rect width="20" height="20" rx="2" fill="#0b6b35"/><path d="M6 4 L8.5 4 L9.5 7.5 L8 8.5 Q9.5 11.5 11.5 12 L12.5 10.5 L16 11.5 L16 14 Q15 16 12.5 15.5 Q5.5 13.5 4.5 7 Q4.5 4.5 6 4 Z" fill="#fff"/></svg>
        0123 456 789
        <svg viewBox="0 0 20 20"><rect width="20" height="20" rx="2" fill="#0b6b35"/><rect x="5" y="3.5" width="10" height="5" fill="none" stroke="#fff" stroke-width="1.4"/><rect x="3.5" y="8" width="13" height="6" rx="1" fill="#fff"/><rect x="6" y="12" width="8" height="4.5" fill="#fff" stroke="#0b6b35" stroke-width="1"/></svg>
        0987 654 321
      </p>
    </section>

    <ul class="honours">
      <li>Most Generous Host of the Province<span class="sep">|</span>Clean Harbour Movement Top Champion</li>
      <li>Most Noted Benefactor of the Region<span class="sep">|</span>Green Transit Pioneer</li>
      <li>Civic Virtue Ambassador<span class="sep">|</span>Urban Renewal Salvage Specialist</li>
      <li>Flood Relief Volunteer Leader<span class="sep">|</span>Most Cheerful Donor of the Year</li>
      <li>Top Ten Most Tireless Neighbour<span class="sep">|</span>Nanjing’s Finest</li>
    </ul>
  </article>
</body>
</html>
```